Holbys Pet Care

Hi. I need a business card /logo for my pet care business. Im thinking about a dogs paw print. Although i do look after other pets so don't want to restrict my self. Open to suggestions on colour etc but like greens and purples.The name of my business is holby's pet care. The logo could be just an image or have holbys power care on it. An option to do either would be great. For the winner i also would like a Web page (word press template if possible) designed if you can, of course I'll pay additional for this. Look forward to your ideas!

```html
<!DOCTYPE html>
<html lang="en">
<head>
<meta charset="utf-8">
<title>Holby's Pet Care – Business Card</title>
<link rel="stylesheet" href="https://fonts.googleapis.com/css2?family=M+PLUS+1p:wght@500&family=Rammetto+One&display=swap">
<style>
  :root {
    --navy: #1f3a8f;
    --sky: #1a8fe0;
    --cloud: #ffffff;
    --grass-light: #b6ef3a;
    --grass: #3fc82a;
    --grass-deep: #1fa51f;
    --sun: #ff1a1a;
    --fur: #d2a45e;
    --fur-light: #e4bd7c;
    --ink: #1b2740;
    --brand-ink: #1c2a8a;
    --paw-grey: #4a4a4a;
  }
  html, body {
    margin: 0;
    padding: 0;
    overflow: hidden;
    background: #ffffff;
  }
  .card {
    position: relative;
    width: 1200px;
    height: 673px;
    overflow: hidden;
    background: var(--navy);
  }
  .card__waves {
    position: absolute;
    inset: 0;
  }
  .card__title {
    position: absolute;
    left: 36px;
    top: 40px;
    margin: 0;
    font-family: "M PLUS 1p", "Helvetica Neue", Arial, sans-serif;
    font-weight: 500;
    font-size: 94px;
    line-height: 1;
    color: var(--cloud);
    letter-spacing: 1px;
  }
  .card__sun {
    position: absolute;
    left: 935px;
    top: 15px;
    width: 165px;
    height: 165px;
    border-radius: 50%;
    background: var(--sun);
  }
  .card__tagline {
    position: absolute;
    left: 458px;
    top: 262px;
    margin: 0;
    font-family: "Rammetto One", "Arial Black", sans-serif;
    font-size: 50px;
    line-height: 1.0;
    color: var(--cloud);
    -webkit-text-stroke: 2px var(--ink);
    text-shadow: 3px 4px 0 var(--ink);
    letter-spacing: 4px;
    white-space: nowrap;
  }
  .card__tagline span {
    display: block;
  }
  .card__tagline .line-two {
    margin-left: 22px;
  }
  .card__illustration {
    position: absolute;
    left: 0;
    top: 210px;
    width: 410px;
    height: 463px;
    background:
      radial-gradient(ellipse 42% 48% at 38% 48%, var(--fur-light) 0%, rgba(210,164,94,0.85) 45%, rgba(210,164,94,0) 75%),
      radial-gradient(ellipse 34% 38% at 62% 70%, rgba(210,164,94,0.8) 0%, rgba(210,164,94,0) 80%);
  }
  .card__brand {
    position: absolute;
    left: 800px;
    top: 562px;
    display: flex;
    align-items: center;
    gap: 16px;
  }
  .card__brand-dot {
    width: 82px;
    height: 82px;
    border-radius: 50%;
    background: var(--paw-grey);
  }
  .card__brand-name {
    font-family: "M PLUS 1p", "Helvetica Neue", Arial, sans-serif;
    font-weight: 500;
    font-size: 30px;
    color: var(--brand-ink);
    white-space: nowrap;
  }
</style>
</head>
<body>
  <main class="card">
    <svg class="card__waves" width="1200" height="673" viewBox="0 0 1200 673" aria-hidden="true">
      <defs>
        <linearGradient id="grass-fill" x1="0" y1="0" x2="0" y2="1">
          <stop offset="0" stop-color="#3fc82a"/>
          <stop offset="1" stop-color="#1fa51f"/>
        </linearGradient>
      </defs>
      <path class="wave wave--sky" fill="var(--sky)"
            d="M0,250 C200,215 330,110 560,130 C780,150 900,250 1200,70 L1200,673 L0,673 Z"/>
      <path class="wave wave--cloud" fill="var(--cloud)"
            d="M0,300 C200,250 340,175 560,190 C780,205 900,310 1200,200 L1200,673 L0,673 Z"/>
      <path class="wave wave--grass-light" fill="var(--grass-light)"
            d="M0,505 C250,470 420,385 620,405 C820,425 950,430 1200,318 L1200,673 L0,673 Z"/>
      <path class="wave wave--grass" fill="url(#grass-fill)"
            d="M0,520 C250,490 420,410 620,430 C820,450 960,455 1200,345 L1200,673 L0,673 Z"/>
    </svg>

    <h1 class="card__title">Holby's Pet Care</h1>

    <div class="card__sun" role="img" aria-label="Red splash sun decoration"></div>

    <p class="card__tagline">
      <span class="line-one">Pet sitting &amp;</span>
      <span class="line-two">dog walking</span>
    </p>

    <div class="card__illustration" role="img" aria-label="Illustration of two golden puppies sitting on the grass, one with a blue collar and one with a red collar"></div>

    <div class="card__brand">
      <span class="card__brand-dot"></span>
      <span class="card__brand-name">Holby's Pet Care</span>
    </div>
  </main>
</body>
</html>
```